Pelbrook Business Cards

Create new business cards with the details below.

Aaron Velst
Director

MB: +61 412 563 904
PH: 1300 417 639
Email: aaron.velst@pelbrook.com.au
Address: 27C Marlow Parade, Campbellfield VIC 3061 Australia
Website: www.pelbrook.com.au

Target Market(s)

Other business

Industry/Entity Type

Business

Requirements
Must have
• must be clean looking

```html
<!DOCTYPE html>
<html lang="en">
<head>
<meta charset="utf-8">
<title>Pelbrook Business Cards</title>
<link rel="stylesheet" href="https://fonts.googleapis.com/css2?family=Ubuntu:wght@400;500;700&display=swap">
<style>
  :root {
    --page-bg: #ece8e1;
    --green-light: #c6e01e;
    --green-mid: #5cc62c;
    --green-deep: #22a238;
    --ink-dark: #3a3a3a;
    --ink-body: #555555;
    --card-white: #f6f6f6;
    --stripe-1: #0f8a3a;
    --stripe-2: #33b24a;
    --stripe-3: #93c92a;
    --stripe-4: #c5dc18;
    --stripe-5: #c9c9c9;
    --stripe-6: #9a9a9a;
    --stripe-7: #3c3c3c;
    --white: #ffffff;
  }
  * { margin: 0; padding: 0; box-sizing: border-box; }
  html, body {
    width: 1200px; height: 1000px; overflow: hidden;
    background: var(--page-bg);
    font-family: "Ubuntu", sans-serif;
  }
  .canvas { position: relative; width: 1200px; height: 1000px; }

  .card {
    position: absolute; left: 323px; width: 545px;
    box-shadow: 0 4px 14px rgba(0,0,0,0.18);
  }

  /* Front */
  .card-front {
    top: 220px; height: 318px;
    background: radial-gradient(ellipse 75% 90% at 50% 8%, var(--green-light) 0%, var(--green-mid) 55%, var(--green-deep) 100%);
  }
  .front-brand {
    position: absolute; left: 109px; top: 138px;
    display: flex; align-items: center; gap: 10px;
  }
  .brand-mark { width: 54px; height: 54px; background: var(--ink-dark); }
  .brand-text { display: flex; flex-direction: column; }
  .front-brand .brand-name {
    font-size: 39px; font-weight: 700; color: var(--white);
    letter-spacing: 0.5px; line-height: 40px;
  }
  .front-brand .brand-tagline {
    font-size: 15px; font-weight: 700; color: var(--ink-dark);
    letter-spacing: 1.6px; margin-top: 2px; padding-left: 2px;
  }
  .front-web {
    position: absolute; left: 0; right: 0; bottom: 16px;
    text-align: center; color: var(--white);
    font-size: 15px; font-weight: 700;
  }

  /* Back */
  .card-back {
    top: 568px; height: 320px;
    background: var(--card-white);
    overflow: hidden;
  }
  .back-brand {
    position: absolute; left: 36px; top: 123px;
    display: flex; align-items: center; gap: 6px;
  }
  .back-brand .brand-mark { width: 33px; height: 33px; }
  .back-brand .brand-name {
    font-size: 24px; font-weight: 700; color: var(--ink-dark); line-height: 24px;
  }
  .back-brand .brand-tagline {
    font-size: 10.5px; font-weight: 700; color: var(--ink-dark);
    letter-spacing: 1px; margin-top: 1px;
  }
  .person {
    position: absolute; right: 307px; top: 188px; text-align: right;
  }
  .person-name { font-size: 16px; font-weight: 700; color: var(--ink-dark); }
  .person-role { font-size: 11px; color: var(--ink-body); margin-top: 1px; }

  .contact {
    position: absolute; left: 294px; top: 90px;
    color: var(--ink-body); font-size: 13.5px;
  }
  .contact-icons { display: flex; gap: 5px; margin-bottom: 8px; }
  .contact-icons svg { width: 20px; height: 20px; display: block; }
  .contact p { line-height: 18px; }
  .contact .gap { margin-top: 9px; }

  .stripe {
    position: absolute; left: 0; right: 0; bottom: 0; height: 13px;
    display: flex; overflow: hidden;
  }
  .stripe span { flex: 1; height: 100%; transform: skewX(-30deg); margin: 0 -2px; }
  .stripe span:first-child { margin-left: -10px; }
  .stripe span:last-child { margin-right: -10px; }
</style>
</head>
<body>
<div class="canvas">

  <section class="card card-front">
    <div class="front-brand">
      <div class="brand-mark"></div>
      <div class="brand-text">
        <span class="brand-name">PELBROOK</span>
        <span class="brand-tagline">PLANTATION SHUTTERS</span>
      </div>
    </div>
    <div class="front-web">www.pelbrook.com.au</div>
  </section>

  <section class="card card-back">
    <div class="back-brand">
      <div class="brand-mark"></div>
      <div class="brand-text">
        <span class="brand-name">PELBROOK</span>
        <span class="brand-tagline">PLANTATION SHUTTERS</span>
      </div>
    </div>

    <div class="person">
      <div class="person-name">Aaron Velst</div>
      <div class="person-role">Director</div>
    </div>

    <div class="contact">
      <div class="contact-icons">
        <svg viewBox="0 0 20 20" aria-label="Phone"><circle cx="10" cy="10" r="10" fill="#33b24a"/><path d="M6.5 5.2c.6-.5 1.2-.3 1.5.2l.9 1.6c.3.5.1 1-.3 1.3l-.5.4c.5 1.2 1.5 2.2 2.7 2.7l.4-.5c.3-.4.9-.5 1.3-.3l1.6.9c.5.3.7.9.2 1.5-.8 1-2 1.2-3.3.6-2-.9-3.8-2.7-4.7-4.7-.6-1.3-.4-2.5.2-3.7z" fill="#fff"/></svg>
        <svg viewBox="0 0 20 20" aria-label="Address"><circle cx="10" cy="10" r="10" fill="#33b24a"/><path d="M10 4.6l5 4.3h-1.5v5.5h-2.4v-3.3h-2.2v3.3H6.5V8.9H5z" fill="#fff"/></svg>
        <svg viewBox="0 0 20 20" aria-label="Email"><circle cx="10" cy="10" r="10" fill="#33b24a"/><rect x="5" y="6.5" width="10" height="7" rx="0.8" fill="#fff"/><path d="M5.3 7l4.7 3.6L14.7 7" fill="none" stroke="#33b24a" stroke-width="1"/></svg>
        <svg viewBox="0 0 20 20" aria-label="Website"><circle cx="10" cy="10" r="10" fill="#33b24a"/><circle cx="10" cy="10" r="4.6" fill="none" stroke="#fff" stroke-width="1.3"/></svg>
      </div>
      <p>M: +61 412 563 904</p>
      <p>P : 1300 417 639</p>
      <p class="gap">27C Marlow Parade</p>
      <p>Kestrelwood VIC 3199 Australia</p>
      <p class="gap">aaron.velst@pelbrook.com.au</p>
      <p class="gap">www.pelbrook.com.au</p>
    </div>

    <div class="stripe">
      <span style="background:var(--stripe-1)"></span>
      <span style="background:var(--stripe-2)"></span>
      <span style="background:var(--stripe-3)"></span>
      <span style="background:var(--stripe-4)"></span>
      <span style="background:var(--stripe-5)"></span>
      <span style="background:var(--stripe-6)"></span>
      <span style="background:var(--stripe-7)"></span>
    </div>
  </section>

</div>
</body>
</html>
```